Pop up exhibition stand 2000mm (H) x 800mm (W)

I would like a simple pop up banner stand for an exhibition.

We need a pop up banner stand design for 'Brindle Forge Services'

the size is 2000mm(H) x 800mm (W)

Ad copy as follows :

[Brindle Forge logo]

From Sheet Metal To Large Sand Castings

Our Capacity and Rapid Quenching drop bottom ovens deliver precise processing.
We also serve the leading names in aerospace, automotive and advanced engineering.

Visit www.brindleforge-example.co.uk/ or call us Tel: +44 (0)1632 960318

[Put the crafted across the shires logo here, also include the text member somewhere close]

check on their website for other ideas that can help you with this project.

Target Market(s)

will be used at a trade show

Requirements
Nice to have
• modern design for UK manufacturing business

```html
<!DOCTYPE html>
<html lang="en">
<head>
<meta charset="utf-8">
<title>Brindle Forge Services – Exhibition Banner</title>
<link href="https://fonts.googleapis.com/css2?family=Open+Sans:ital,wght@0,400;0,600;0,700;1,400&display=swap" rel="stylesheet">
<style>
  :root {
    --brand-red: #d2232e;
    --deep-red: #b81c26;
    --ink: #3a3a3a;
    --body-grey: #555a5f;
    --soft-grey: #8a8d90;
    --panel-light: #f4f4f4;
    --panel-mid: #dcdcdc;
    --rule: #cfcfcf;
    --white: #ffffff;
  }
  * { margin: 0; padding: 0; box-sizing: border-box; }
  html, body { width: 1200px; height: 2984px; overflow: hidden; }
  body {
    position: relative;
    font-family: "Open Sans", Arial, sans-serif;
    background: linear-gradient(180deg, var(--panel-mid) 0%, var(--panel-light) 40%, var(--panel-mid) 100%);
    color: var(--ink);
  }
  .band { position: absolute; left: 0; width: 1200px; background: var(--brand-red); }
  .band--top { top: 0; height: 32px; }
  .band--bottom { bottom: 0; height: 136px; }

  .header-shape { position: absolute; top: 32px; left: 0; }

  .brand-name {
    position: absolute; top: 100px; left: 90px;
    display: flex; align-items: center; gap: 26px;
    font-size: 92px; font-weight: 700; color: var(--deep-red); line-height: 1;
    white-space: nowrap;
  }
  .brand-dot { width: 60px; height: 60px; border-radius: 50%; background: var(--deep-red); flex: none; }
  .tagline {
    position: absolute; top: 236px; left: 430px;
    font-size: 54px; line-height: 1.15; font-style: italic; white-space: nowrap;
  }
  .tagline__lead { color: var(--soft-grey); display: block; }
  .tagline__main { color: var(--brand-red); display: block; }

  .headline {
    position: absolute; top: 560px; left: 0; width: 1200px;
    text-align: center; color: var(--brand-red); font-weight: 400; line-height: 1.1;
  }
  .headline__small { font-size: 66px; }
  .headline__big { font-size: 104px; }

  .photo { position: absolute; border: 6px solid var(--white); }
  .photo--hero { top: 828px; left: 40px; width: 1120px; height: 752px;
    background: linear-gradient(135deg, #2d4f6e 0%, #3f86b0 45%, #b9c2c6 100%); }
  .photo--left { top: 2108px; left: 40px; width: 548px; height: 452px;
    background: linear-gradient(135deg, #c8c3be 0%, #9aa0a4 60%, #6d7276 100%); }
  .photo--right { top: 2108px; left: 612px; width: 548px; height: 452px;
    background: linear-gradient(135deg, #8f8f88 0%, #b7b9b6 50%, #d9d9d6 100%); }

  .sectors { position: absolute; top: 1596px; left: 0; width: 1200px; height: 150px; }
  .sector { position: absolute; width: 300px; text-align: center; }
  .sector svg { display: block; margin: 0 auto; }
  .sector__label { font-size: 26px; font-weight: 700; color: var(--ink); letter-spacing: 0.5px; margin-top: 6px; }

  .intro {
    position: absolute; top: 1770px; left: 50px; width: 1110px;
    font-size: 48px; line-height: 78px; color: var(--body-grey);
  }
  .intro strong { color: var(--ink); font-weight: 700; }

  .footer { position: absolute; top: 2580px; left: 0; width: 1200px; height: 268px; background: var(--white); }
  .contact-row {
    position: absolute; top: 26px; left: 0; width: 1200px; height: 70px;
    display: flex; align-items: center; justify-content: center; gap: 30px;
  }
  .contact { display: flex; align-items: center; gap: 14px; font-size: 34px; color: var(--ink); white-space: nowrap; }
  .divider { background: var(--rule); width: 3px; flex: none; }
  .divider--contact { height: 60px; }

  .member-row {
    position: absolute; top: 134px; left: 0; width: 1200px; height: 116px;
    display: flex; align-items: center; justify-content: center; gap: 26px;
  }
  .member-label { font-size: 38px; color: var(--ink); }
  .divider--member { height: 110px; }
  .member-badge { width: 104px; height: 104px; border-radius: 50%; background: var(--brand-red); flex: none; }
  .member-name { font-size: 42px; line-height: 1.1; color: var(--brand-red); text-transform: uppercase; white-space: nowrap; }
</style>
</head>
<body>
  <div class="band band--top"></div>

  <svg class="header-shape" width="1200" height="460" viewBox="0 0 1200 460" aria-hidden="true">
    <defs>
      <linearGradient id="headerFill" x1="0" y1="0" x2="0" y2="1">
        <stop offset="0" stop-color="#d8d8d8"/>
        <stop offset="1" stop-color="#ffffff"/>
      </linearGradient>
    </defs>
    <polygon points="0,0 1200,0 1200,380 600,450 0,380" fill="url(#headerFill)"/>
  </svg>

  <div class="brand-name"><span class="brand-dot"></span>Brindle Forge</div>
  <p class="tagline">
    <span class="tagline__lead">the solution in</span>
    <span class="tagline__main">aluminium heat treatment</span>
  </p>

  <h1 class="headline">
    <span class="headline__small">From </span><span class="headline__big">Sheet Metal</span><span class="headline__small"> To</span><br>
    <span class="headline__big">Large Sand Castings</span>
  </h1>

  <div class="photo photo--hero" role="img" aria-label="Engineer inspecting a large cast aluminium ring in front of a blue drop bottom quench oven"></div>

  <div class="sectors">
    <div class="sector" style="left:30px">
      <svg width="180" height="90" viewBox="0 0 180 90" aria-hidden="true">
        <path d="M10 60 L150 22 Q172 18 170 30 Q168 38 150 42 L40 70 Z" fill="var(--brand-red)"/>
        <path d="M70 44 L110 10 L128 8 L100 38 Z M80 60 L112 82 L126 82 L104 54 Z M20 58 L12 40 L24 40 L36 54 Z" fill="var(--brand-red)"/>
      </svg>
      <div class="sector__label">AEROSPACE</div>
    </div>
    <div class="sector" style="left:450px">
      <svg width="180" height="90" viewBox="0 0 180 90" aria-hidden="true">
        <path d="M20 62 L20 46 Q22 38 34 36 L56 16 Q62 12 72 12 L112 12 Q122 12 128 18 L150 36 Q164 38 166 48 L166 62 Z" fill="var(--brand-red)"/>
        <path d="M64 22 L84 22 L84 36 L50 36 Z M94 22 L112 22 L128 36 L94 36 Z" fill="#fff"/>
        <circle cx="52" cy="64" r="15" fill="var(--brand-red)" stroke="#fff" stroke-width="5"/>
        <circle cx="134" cy="64" r="15" fill="var(--brand-red)" stroke="#fff" stroke-width="5"/>
      </svg>
      <div class="sector__label">AUTOMOTIVE</div>
    </div>
    <div class="sector" style="left:860px">
      <svg width="180" height="90" viewBox="0 0 180 90" aria-hidden="true">
        <path d="M20 88 L20 46 L60 24 L60 46 L100 24 L100 46 L130 30 L130 4 L152 4 L152 88 Z" fill="var(--brand-red)"/>
        <rect x="34" y="58" width="14" height="12" fill="#fff"/>
        <rect x="62" y="58" width="14" height="12" fill="#fff"/>
        <rect x="90" y="58" width="14" height="12" fill="#fff"/>
      </svg>
      <div class="sector__label">ENGINEERING</div>
    </div>
  </div>

  <p class="intro">Our <strong>Capacity</strong> and <strong>Rapid Quenching</strong> drop bottom ovens deliver <strong>precise</strong> processing.&nbsp; We also serve the <strong>leading</strong> names in aerospace, automotive and advanced engineering.</p>

  <div class="photo photo--left" role="img" aria-label="Company representative standing beside racks of heat treated aluminium parts"></div>
  <div class="photo photo--right" role="img" aria-label="Team member reviewing paperwork beside a heat treatment oven in the workshop"></div>

  <footer class="footer">
    <div class="contact-row">
      <div class="contact contact--web">
        <svg width="40" height="28" viewBox="0 0 44 30" aria-hidden="true">
          <path d="M4 15 L28 15 M20 6 L30 15 L20 24" fill="none" stroke="var(--ink)" stroke-width="4" stroke-linecap="round" stroke-linejoin="round"/>
        </svg>
        <span>www.brindleforge-example.co.uk</span>
      </div>
      <div class="divider divider--contact"></div>
      <div class="contact contact--phone">
        <svg width="34" height="34" viewBox="0 0 36 36" aria-hidden="true">
          <circle cx="18" cy="18" r="15" fill="none" stroke="var(--ink)" stroke-width="3"/>
          <path d="M12 10 Q10 18 18 25 L22 22 L19 18 L16 19 Q14 16 15 13 L17 12 L14 9 Z" fill="var(--ink)"/>
        </svg>
        <span>+44 (0)1632 960318</span>
      </div>
    </div>

    <div class="member-row">
      <div class="member-label">Member</div>
      <div class="divider divider--member"></div>
      <div class="member-badge"></div>
      <div class="member-name">Crafted across<br>the shires</div>
    </div>
  </footer>

  <div class="band band--bottom"></div>
</body>
</html>
```